Massage-Creme label for a young pharmacy

We are a young pharmacy which is part of a big union. We developed for a customer a very good massage creme with aloe vera, coconut oil, and many more advantages and as well a massage jelly. All we need is a good and affordable label which is beatiful and helps us to promote our product. As we want to develop further products, it would be very cool to have a corporate label for all upcoming products.

Target Market(s)

professional masseurs and physiotherapists

Industry/Entity Type

Health And Wellness

Font styles to use
Sans Serif
Decorative

Colors

Designer to choose colors to be used in the design.

Requirements
Must have
• Professionally looking design (but I'm sure you are doing so... :-)
Nice to have
• Label can have any shape. What you see is just a bad label with corresponding sizes, so you can imagine how it would look like in the final state.
Should not have
• If possible, the label should not be completely black (although it might look cool) as we are printing it on our own Vostek qr318-ux and black is difficult to print (and very costy).

```html
<!DOCTYPE html>
<html lang="de">
<head>
<meta charset="utf-8">
<title>Massage-Crème Etikett</title>
<link href="https://fonts.googleapis.com/css2?family=Roboto+Condensed:wght@400;700&family=Yellowtail&display=swap" rel="stylesheet">
<style>
  :root {
    --stage: #eef1ec;
    --green-top: #2b873c;
    --green-mid: #3a8e3a;
    --green-bottom: #88ad3b;
    --white: #ffffff;
    --ink: #1c1c1c;
    --badge-red: #d8252c;
    --aloe: #4fae4a;
    --coconut: #a8744a;
  }
  * { box-sizing: border-box; margin: 0; padding: 0; }
  html, body { width: 1200px; height: 900px; overflow: hidden; }
  body {
    background: var(--stage);
    font-family: "Roboto Condensed", Arial, sans-serif;
    color: var(--white);
    position: relative;
  }
  .label {
    position: absolute; left: 60px; top: 16px;
    width: 1080px; height: 868px;
    overflow: hidden;
    background: linear-gradient(180deg, var(--green-top) 0%, var(--green-mid) 45%, var(--green-bottom) 100%);
  }
  .title-oval {
    position: absolute; left: 47px; top: 56px;
    width: 470px; height: 208px;
    background: var(--white); border-radius: 50%;
    color: var(--ink); text-align: center;
    overflow: hidden;
    display: flex; flex-direction: column; align-items: center; justify-content: center;
  }
  .product-name {
    font-family: "Yellowtail", cursive;
    font-size: 58px; font-weight: 400;
    line-height: 1.1; white-space: nowrap;
    max-width: 400px;
  }
  .product-variant {
    display: flex; align-items: center; justify-content: center; gap: 22px;
    margin-top: 20px; font-size: 14px; letter-spacing: 0.5px;
  }
  .product-variant::before, .product-variant::after {
    content: ""; width: 70px; height: 2px; background: var(--ink);
  }
  .badge {
    position: absolute; left: 66px; top: 300px;
    width: 140px; height: 100px;
    transform: rotate(-28deg);
  }
  .badge svg { position: absolute; inset: 0; }
  .badge-text {
    position: absolute; inset: 0;
    display: flex; align-items: center; justify-content: center; text-align: center;
    color: var(--ink); font-size: 15px; line-height: 1.05;
  }
  .ingredients-art {
    position: absolute; left: 74px; top: 470px;
    width: 400px; height: 330px;
    border-radius: 40% 50% 30% 35%;
    background: radial-gradient(ellipse at 35% 60%, var(--aloe) 0%, rgba(79,174,74,0.6) 45%, transparent 70%),
                radial-gradient(ellipse at 62% 45%, var(--coconut) 0%, rgba(168,116,74,0.5) 30%, transparent 55%);
  }
  .info {
    position: absolute; left: 620px; top: 98px; width: 400px;
    text-align: center; font-size: 15px; line-height: 1.2;
  }
  .info p { margin-bottom: 22px; }
  .ph-line {
    display: inline-block; padding: 0 14px 6px;
    border-bottom: 2px solid var(--white);
  }
  .quality-note { font-size: 11.5px; margin-top: 28px; }
  .free-from {
    margin: 8px auto 0; width: 320px; padding: 8px 10px;
    border: 2px solid var(--white); font-size: 12px;
  }
  .pharmacy-name {
    position: absolute; left: 820px; top: 670px;
    display: flex; align-items: center; gap: 8px;
    font-size: 15px; font-weight: 400;
  }
  .pharmacy-name .mark { width: 10px; height: 10px; background: var(--white); }
  .batch {
    position: absolute; left: 640px; top: 716px;
    font-size: 11px; line-height: 1.25;
  }
  .composition {
    position: absolute; left: 640px; top: 756px; width: 370px;
    font-size: 8.5px; line-height: 1.25;
  }
  .volume {
    position: absolute; left: 788px; top: 816px; font-size: 16px;
  }
</style>
</head>
<body>
  <main class="label">
    <div class="title-oval">
      <h1 class="product-name">Massage-Crème</h1>
      <div class="product-variant">COCONUT - ALOE VERA</div>
    </div>

    <div class="badge">
      <svg viewBox="0 0 140 100" aria-hidden="true">
        <polygon fill="#ffffff" stroke="#d8252c" stroke-width="3" stroke-dasharray="4 2"
          points="70,4 80,14 94,8 100,20 116,18 116,32 132,36 124,50 134,62 120,70 122,84 106,84 100,96 86,90 70,98 56,90 40,96 34,84 18,84 20,70 6,62 16,50 8,36 24,32 24,18 40,20 46,8 60,14"/>
      </svg>
      <div class="badge-text">energetisch<br>leitend !</div>
    </div>

    <div class="ingredients-art" role="img" aria-label="Illustration: Aloe-Vera-Blätter, aufgeschlagene Kokosnuss und Fläschchen mit Kokosöl"></div>

    <section class="info">
      <p>Hochwertige und sehr hautschonende Emulsion mit hervorragendem Gleitverhalten für die professionelle Massage.</p>
      <p>Hilft durch den hohen Gehalt an Aloe Vera-Gel (50%), die Feuchtigkeit der Haut zu erhalten und schützt durch die Zugabe von Panthenol (= Provitamin B5) und Allantoin vor Hautreizungen.</p>
      <p>Speziell für die (bio-)energetische Massage entwickelt.</p>
      <p><span class="ph-line">pH-neutral für die Haut (pH-Wert = 5.5)</span></p>
      <p class="quality-note">Bei der Entwicklung unserer Produkte legen wir grössten Wert auf gute Verträglichkeit und hochwertige Rohstoffe.</p>
      <div class="free-from">Dieses Produkt ist frei von Parabenen, Mineralölen (Paraffin/Vaseline), Silikonen, Farbstoffen und Mikroplastik (Acrylate).</div>
    </section>

    <div class="pharmacy-name"><span class="mark"></span>Vitalis Apotheke</div>

    <div class="batch">Exp: 03/2021<br>Lot: 913015/A</div>

    <p class="composition">Zus: water (aqua), cetearyl isononanoate, ethylhexyl stearate, cocos nucifera (coconut oil), octyldodecanol, glyceryl stearate citrate, cetearyl alcohol, phenoxyethanol (and) caprylyl glycol, panthenol, sodium chloride, xanthan gum, disodium hydrogenphosphate, citric acid, aloe barbadensis leaf juice extract, allantoin, parfum</p>

    <div class="volume">℮ 1000 ml</div>
  </main>
</body>
</html>
```